Business Card Design

Business card design.

Business card is to have logo, website address and email address.

Website is www.brightkettle.ie
Email is info@brightkettle.ie
Logo uploaded

I have ordered Business Card Printing via Print Harbor, the Double-sided colour printed option with gloss finish.

Industry/Entity Type

Business

```html
<!DOCTYPE html>
<html lang="en">
<head>
<meta charset="utf-8">
<title>Bright Kettle – Business Card</title>
<link rel="stylesheet" href="https://fonts.googleapis.com/css2?family=Open+Sans:wght@400;600;700;800&display=swap">
<style>
  :root {
    --page-bg: #e9e6e1;
    --card-black: #121212;
    --card-glow: #555555;
    --accent-red: #d3222a;
    --text-white: #ffffff;
    --text-soft: #e6e6e6;
  }
  * { box-sizing: border-box; margin: 0; padding: 0; }
  html, body { width: 1200px; height: 903px; overflow: hidden; }
  body {
    background: var(--page-bg);
    font-family: "Open Sans", Arial, sans-serif;
    display: flex;
    flex-direction: column;
    align-items: center;
    justify-content: center;
    gap: 40px;
  }
  .card {
    position: relative;
    width: 700px;
    height: 400px;
    border-radius: 4px;
    box-shadow: 0 10px 28px rgba(0,0,0,0.28);
    overflow: hidden;
  }
  .card--front {
    background: radial-gradient(ellipse 340px 230px at 250px 190px, var(--card-glow) 0%, #2a2a2a 45%, var(--card-black) 85%);
  }
  .card--back {
    background: radial-gradient(ellipse 320px 220px at 170px 300px, var(--card-glow) 0%, #262626 45%, var(--card-black) 85%);
  }
  .brand {
    position: absolute;
    display: flex;
    align-items: center;
    gap: 12px;
  }
  .brand__dot {
    width: 34px; height: 34px;
    border-radius: 50%;
    background: var(--accent-red);
    flex: none;
  }
  .brand__name {
    color: var(--text-white);
    font-weight: 800;
    font-size: 38px;
    letter-spacing: -0.5px;
    line-height: 1;
  }
  .card--front .brand { left: 70px; top: 150px; }
  .front__web {
    position: absolute;
    left: 70px; width: 430px;
    top: 205px;
    text-align: right;
    color: var(--text-soft);
    font-size: 17px;
    letter-spacing: 0.3px;
  }
  .accent-line {
    position: absolute;
    height: 6px;
    background: var(--accent-red);
  }
  .card--front .accent-line { left: 70px; right: 60px; top: 290px; }

  .card--back .brand { left: 40px; top: 290px; }
  .card--back .brand__name { font-size: 30px; }
  .card--back .brand__dot { width: 28px; height: 28px; }
  .contact {
    position: absolute;
    left: 330px;
    top: 70px;
    color: var(--text-white);
  }
  .contact__name { font-weight: 700; font-size: 22px; line-height: 1.1; }
  .contact__role { color: var(--accent-red); font-size: 14px; margin-bottom: 16px; }
  .contact__list { list-style: none; }
  .contact__item {
    display: flex; align-items: center; gap: 12px;
    font-size: 17px; color: var(--text-soft);
    margin-bottom: 8px;
  }
  .contact__icon { width: 18px; height: 18px; flex: none; fill: var(--accent-red); }
  .card--back .accent-line { left: 330px; right: 40px; top: 240px; }
</style>
</head>
<body>
  <section class="card card--front" aria-label="Card front">
    <div class="brand">
      <span class="brand__dot"></span>
      <span class="brand__name">BRIGHTKETTLE.IE</span>
    </div>
    <p class="front__web">www.brightkettle.ie</p>
    <div class="accent-line"></div>
  </section>

  <section class="card card--back" aria-label="Card back">
    <div class="contact">
      <p class="contact__name">Alan Marsh</p>
      <p class="contact__role">General Manager</p>
      <ul class="contact__list">
        <li class="contact__item">
          <svg class="contact__icon" viewBox="0 0 24 24" aria-hidden="true"><path d="M6.6 10.8a15.1 15.1 0 0 0 6.6 6.6l2.2-2.2c.3-.3.7-.4 1-.2 1.1.4 2.3.6 3.6.6.6 0 1 .4 1 1V20c0 .6-.4 1-1 1A17 17 0 0 1 3 4c0-.6.4-1 1-1h3.5c.6 0 1 .4 1 1 0 1.3.2 2.5.6 3.6.1.3 0 .7-.2 1z"/></svg>
          (000) 555-014
        </li>
        <li class="contact__item">
          <svg class="contact__icon" viewBox="0 0 24 24" aria-hidden="true"><path d="M2 5h20v14H2zm2 2v.5l8 5 8-5V7zm0 2.8V17h16V9.8l-8 5z"/></svg>
          info@brightkettle.ie
        </li>
        <li class="contact__item">
          <svg class="contact__icon" viewBox="0 0 24 24" aria-hidden="true"><circle cx="12" cy="12" r="10"/><path d="M2 12h20M12 2c3 3 3 17 0 20M12 2c-3 3-3 17 0 20" stroke="#121212" stroke-width="1.6" fill="none"/></svg>
          www.brightkettle.ie
        </li>
      </ul>
    </div>
    <div class="accent-line"></div>
    <div class="brand">
      <span class="brand__dot"></span>
      <span class="brand__name">BRIGHTKETTLE.IE</span>
    </div>
  </section>
</body>
</html>
```